Postcard, Gift Card/Envelope
Looking for Trendy and Sexy material to represent a High End Salon and Spa.
I'd like to wrap up this project before the expiration ... please put forth your best efforts sooner rather than later.
RT3192 - I love your use of the salon pics on the back!! The front: the main message "We Have Moved!" doesn't jump out to the reader.
Thanks, Few things. Postcard: I like the impact of the new "we have moved", but types style might clash a bit? Envelope: Add the hawthorne location and phone numbers on olutside, but you can make them smaller ... and Make "look and feel your best" in italics. Giftcard: must have two phone numbers underneath the addresses (they are two separate locations). Last, we recently rebranded ... so add "formerly Marisol Glow Studio" in italics below the main logo of the postcard.
Thanks for the fine efforts. For the back of postcard, I like draft #1 with the offer featured on top. I was thinking that the front could have a smaller element "TAN FREE (see offer on back") that doesn’t take away from the clean look of the front. I’d also like to promote and in store promotional, FREE LEG TAN THURDSAY (every Thursday till March 15). I added a pic of the leg tanner to include if you think it won’t be too busy. I also added another pic of the tanning booths that might be used (only at your discretion)
The Gift card should be one sided, needs to include address/phones of both salons and add a line for Date. Try using a more luxurious font to represent the quality of the business. The envelope is not for mailing, simply for presentation … so perhaps use the graphics that you used for the “other side” of the gift card with the tag line “Look and Feel Your Best”.
Thanks! When you get a chance can you check your messages in the top right-hand corner of the page
Thanks for your submission. I like it. I'd like to reference to the Free week offer somewhere on the front. Also, see if there is a way to make the "We Have Moved" even more prominent. I think it's fairly prominent in your first draft, but want to see a few different levels of POP.

```html
<!DOCTYPE html>
<html lang="en">
<head>
<meta charset="utf-8">
<title>Solara Tan &amp; Spa – Print Set</title>
<link rel="stylesheet" href="https://fonts.googleapis.com/css2?family=Great+Vibes&family=Montserrat:wght@400;600;700;800&display=swap">
<style>
  :root {
    --magenta: #d6177f;
    --magenta-dark: #a80f62;
    --green: #7cb82f;
    --yellow: #f2d21b;
    --orange: #f7941d;
    --ink: #3a3a3a;
    --grey: #8a8a8a;
    --paper: #ffffff;
    --board-a: #3b3b3b;
    --board-b: #1c1c1c;
    --sans: "Montserrat", Arial, sans-serif;
    --script: "Great Vibes", cursive;
  }
  * { box-sizing: border-box; margin: 0; padding: 0; }
  html, body { width: 1200px; height: 784px; overflow: hidden; }
  body {
    position: relative;
    background: linear-gradient(135deg, var(--board-a), var(--board-b));
    font-family: var(--sans);
    color: var(--ink);
  }
  .piece-label {
    position: absolute;
    color: #fff;
    font-size: 15px;
    font-weight: 600;
    letter-spacing: 0.5px;
    text-transform: uppercase;
  }
  .piece {
    position: absolute;
    background: var(--paper);
    overflow: hidden;
    box-shadow: 0 6px 18px rgba(0,0,0,0.5);
  }
  .brand {
    position: absolute;
    display: flex;
    align-items: center;
    gap: 6px;
    font-family: var(--sans);
    font-weight: 800;
    color: var(--green);
    letter-spacing: 0.3px;
    white-space: nowrap;
  }
  .brand-dot { border-radius: 50%; background: var(--orange); flex: none; }
  .photo { position: absolute; }
  .small { position: absolute; font-size: 8px; color: var(--grey); line-height: 1.4; }

  /* postcard front */
  .front { left: 31px; top: 41px; width: 502px; height: 326px; }
  .front .brand { left: 12px; top: 28px; font-size: 12px; }
  .front .brand-dot { width: 10px; height: 10px; }
  .front-tagline { position: absolute; left: 176px; top: 14px; color: var(--magenta); font-size: 10px; line-height: 1.15; }
  .front-tagline strong { display: block; font-size: 15px; font-weight: 800; }
  .front-tagline em { font-family: var(--script); font-style: normal; font-size: 15px; }
  .moved-band {
    position: absolute; left: 0; top: 70px; width: 228px; height: 34px;
    background: var(--magenta); color: #fff;
    font-family: var(--script); font-size: 28px; line-height: 34px; padding-left: 14px;
  }
  .front .map { left: 14px; top: 118px; width: 100px; height: 60px; background: linear-gradient(135deg, #eef2e6, #d9e3cf); border: 1px solid #ccc; }
  .front .address { left: 122px; top: 128px; }
  .front .salon-a { left: 12px; top: 200px; width: 96px; height: 64px; background: linear-gradient(135deg, #c9a88e, #7d5c4a); border: 3px solid #fff; box-shadow: 0 2px 5px rgba(0,0,0,.3); }
  .front .salon-b { left: 116px; top: 190px; width: 72px; height: 74px; background: linear-gradient(135deg, #e9c7d7, #b37a95); border: 3px solid #fff; box-shadow: 0 2px 5px rgba(0,0,0,.3); }
  .front .model { left: 290px; top: 0; width: 212px; height: 326px; background: linear-gradient(160deg, #9ec9e4 0%, #6aa0c8 40%, #c79a7a 70%, #5d4333 100%); }
  .offer-circle {
    position: absolute; left: 196px; top: 182px; width: 96px; height: 96px; border-radius: 50%;
    background: var(--magenta); color: #fff; text-align: center;
    display: flex; align-items: center; justify-content: center;
    font-size: 11px; font-weight: 700; line-height: 1.15; border: 3px solid #fff; box-shadow: 0 2px 6px rgba(0,0,0,.3);
  }
  .offer-circle span { font-size: 15px; font-weight: 800; display: block; }
  .front .contacts { left: 302px; top: 262px; color: #fff; }

  /* gift certificate */
  .gift { left: 593px; top: 101px; width: 578px; height: 230px; }
  .gift .brand { left: 150px; top: 28px; font-size: 18px; }
  .gift .brand-dot { width: 12px; height: 12px; }
  .gift-fields { position: absolute; left: 48px; top: 74px; width: 220px; font-size: 10px; color: var(--grey); }
  .gift-fields div { display: flex; align-items: flex-end; gap: 8px; height: 24px; }
  .gift-fields i { flex: 1; border-bottom: 1px solid #bbb; height: 1px; }
  .gift .tagline { position: absolute; left: 404px; top: 14px; color: var(--ink); font-size: 12px; font-style: italic; }
  .gift .tagline span { font-family: var(--script); font-style: normal; font-size: 26px; color: var(--magenta); }
  .gift .products { left: 400px; top: 50px; width: 178px; height: 130px; background: linear-gradient(135deg, #f4f6ef, #b6d58a 55%, #6e6e6e); }
  .gift-band {
    position: absolute; left: 0; top: 182px; width: 578px; height: 30px; background: var(--magenta);
    color: #fff; font-size: 17px; letter-spacing: 4px; line-height: 30px; padding-left: 14px;
  }
  .gift-band .small { left: 300px; top: 6px; color: #fff; letter-spacing: 0; font-size: 7px; line-height: 1.3; }

  /* postcard back */
  .back { left: 31px; top: 456px; width: 502px; height: 293px; }
  .back .brand { left: 24px; top: 20px; font-size: 18px; }
  .back .brand-dot { width: 12px; height: 12px; }
  .services-title { position: absolute; left: 48px; top: 56px; font-family: var(--script); font-size: 26px; color: var(--magenta); }
  .service { position: absolute; left: 22px; display: flex; align-items: center; gap: 8px; font-size: 8px; color: var(--grey); }
  .service .photo { position: static; width: 26px; height: 28px; background: linear-gradient(135deg, #e0b9a3, #8c5e4a); }
  .leg-tan { position: absolute; left: 22px; top: 192px; color: var(--magenta); font-size: 13px; font-weight: 700; }
  .leg-tan small { display: block; font-size: 7px; font-weight: 400; color: var(--grey); }
  .back-band { position: absolute; left: 0; bottom: 0; }
  .back-slogan { position: absolute; left: 18px; top: 236px; color: #fff; font-size: 22px; font-weight: 800; line-height: 1; }
  .back-slogan em { display: block; font-family: var(--script); font-style: normal; font-size: 18px; font-weight: 400; }
  .back .divider { position: absolute; left: 256px; top: 14px; height: 265px; border-left: 1px dashed #ccc; }
  .back .stamp { position: absolute; right: 18px; top: 14px; width: 44px; height: 52px; border: 1px solid #999; }
  .back .return { left: 266px; top: 16px; font-size: 8px; }

  /* envelope */
  .envelope { left: 593px; top: 461px; width: 578px; height: 254px; }
  .envelope .brand { left: 372px; top: 174px; font-size: 16px; }
  .envelope .brand-dot { width: 11px; height: 11px; }
  .envelope .small { left: 372px; top: 196px; width: 196px; font-size: 6.5px; line-height: 1.35; }
  .stripe { position: absolute; left: 0; width: 578px; }
</style>
</head>
<body>

  <div class="piece-label" style="left:205px; top:12px;">Postcard front</div>
  <div class="piece-label" style="left:815px; top:71px;">Gift certificate</div>
  <div class="piece-label" style="left:205px; top:426px;">Postcard back</div>
  <div class="piece-label" style="left:868px; top:431px;">Envelope</div>

  <!-- Postcard front -->
  <section class="piece front">
    <div class="brand"><span class="brand-dot"></span>SOLARA TAN &amp; SPA</div>
    <div class="front-tagline">New Salon<strong>LARGER</strong>and<br><em>More Luxurious</em></div>
    <div class="moved-band">We Have Moved!</div>
    <div class="photo map" role="img" aria-label="Street map showing the new salon location"></div>
    <div class="small address">128 Linden Ave<br>Suite 4, Brookvale</div>
    <div class="photo salon-a" role="img" aria-label="Photo of the new salon reception"></div>
    <div class="photo salon-b" role="img" aria-label="Photo of a salon treatment room"></div>
    <svg style="position:absolute;left:0;top:276px" width="290" height="50" viewBox="0 0 290 50" aria-hidden="true">
      <path d="M0 10 Q145 50 290 36 L290 50 L0 50 Z" fill="var(--magenta)"/>
    </svg>
    <div class="photo model" role="img" aria-label="Photo of a tanned woman in a bikini by a pool"></div>
    <div class="offer-circle"><div><span>One FREE</span>week of tanning</div></div>
    <div class="small contacts">555-0142<br>book online<br>open daily</div>
  </section>

  <!-- Gift certificate -->
  <section class="piece gift">
    <div class="brand"><span class="brand-dot"></span>SOLARA TAN &amp; SPA</div>
    <div class="gift-fields">
      <div>To<i></i></div>
      <div>From<i></i></div>
      <div>Date<i></i></div>
      <div>Amount<i></i></div>
    </div>
    <div class="tagline">Look &amp; Feel <span>your Best</span></div>
    <div class="photo products" role="img" aria-label="Photo of spa products, towels and a green leaf"></div>
    <div class="gift-band">GIFT CERTIFICATE
      <div class="small">128 Linden Ave · 555-0142<br>40 Orchard St · 555-0187</div>
    </div>
  </section>

  <!-- Postcard back -->
  <section class="piece back">
    <div class="brand"><span class="brand-dot"></span>SOLARA TAN &amp; SPA</div>
    <div class="services-title">Services:</div>
    <div class="service" style="top:92px"><div class="photo" role="img" aria-label="Photo of airbrush tanning"></div>Custom Airbrush</div>
    <div class="service" style="top:124px"><div class="photo" role="img" aria-label="Photo of tanning booths"></div>Stand-up Booths</div>
    <div class="service" style="top:156px"><div class="photo" role="img" aria-label="Photo of the leg tanner"></div>Leg Tanner</div>
    <div class="leg-tan">FREE LEG TAN THURSDAY<small>every Thursday till March 15</small></div>
    <svg class="back-band" width="256" height="72" viewBox="0 0 256 72" aria-hidden="true">
      <path d="M0 0 Q140 24 256 6 L256 72 L0 72 Z" fill="var(--magenta)"/>
    </svg>
    <div class="back-slogan">LARGER<em>and More Luxurious</em></div>
    <div class="divider"></div>
    <div class="small return">Solara Tan &amp; Spa<br>128 Linden Ave<br>Brookvale</div>
    <div class="stamp"></div>
  </section>

  <!-- Envelope -->
  <section class="piece envelope">
    <div class="brand"><span class="brand-dot"></span>SOLARA TAN &amp; SPA</div>
    <div class="small">128 Linden Ave · 555-0142<br>40 Orchard St, Brookvale · 555-0187</div>
    <div class="stripe" style="top:224px;height:5px;background:var(--green)"></div>
    <div class="stripe" style="top:231px;height:5px;background:var(--yellow)"></div>
    <div class="stripe" style="top:238px;height:4px;background:var(--magenta)"></div>
  </section>

</body>
</html>
```